Brightwire Hollow Business cards

one side I would like my logo (uploaded) and the other side I want my details. I'm an electrician in sydney. The logo side I'm happy with just a white background and our logo in the middle.

Details for other side
24/7 Sydney Electrician
Marcus Pell
0431 587 219
marcus@brightwirehollow.com.au
brightwirehollow.com.au
icons for facebook, instagram, linked in

Industry/Entity Type

electrician

Contact Information for Business Card

company info

```html
<!DOCTYPE html>
<html lang="en">
<head>
<meta charset="utf-8">
<title>Brightwire Hollow – Business Cards</title>
<link rel="stylesheet" href="https://fonts.googleapis.com/css2?family=Montserrat:wght@500;700;800&family=Lato:wght@400;700&display=swap">
<style>
  :root{
    --backdrop:#2a2b2e;
    --card:#ffffff;
    --ink:#111111;
    --red:#e8352a;
    --muted:#6b6b6b;
  }
  *{box-sizing:border-box;margin:0;padding:0}
  html,body{width:1200px;height:952px;overflow:hidden;background:var(--backdrop)}
  .canvas{position:relative;width:1200px;height:952px}
  .card{position:absolute;width:540px;height:308px;background:var(--card);border-radius:3px;overflow:hidden;box-shadow:0 14px 34px rgba(0,0,0,.45)}
  .card--logo{left:60px;top:500px}
  .card--details{left:600px;top:150px}

  /* logo side */
  .brand{position:absolute;left:0;right:0;top:112px;text-align:center;font-family:'Montserrat',sans-serif;font-weight:800;font-size:40px;letter-spacing:1px;color:var(--red);text-transform:uppercase;line-height:1}
  .edge-rule{position:absolute;left:0;top:268px;width:540px;height:4px}
  .edge-rule__dark{position:absolute;left:0;top:0;width:220px;height:3px;background:var(--ink)}
  .edge-rule__red{position:absolute;left:228px;top:0;width:312px;height:4px;background:var(--red)}

  /* details side */
  .frame{position:absolute;left:0;top:0}
  .name{position:absolute;left:118px;top:52px;font-family:'Montserrat',sans-serif;font-weight:500;font-size:32px;letter-spacing:1px;color:var(--ink);text-transform:uppercase;line-height:1}
  .name__last{color:var(--red);font-weight:800}
  .tagline{position:absolute;left:112px;top:232px;font-family:'Montserrat',sans-serif;font-weight:800;font-size:15px;letter-spacing:.5px;color:var(--ink);text-transform:uppercase}
  .social{position:absolute;left:200px;top:128px;display:flex;gap:8px}
  .social__dot{width:22px;height:22px;border-radius:50%;background:var(--ink)}
  .contacts{position:absolute;left:300px;top:124px;list-style:none;font-family:'Lato',sans-serif;font-size:12px;color:var(--muted)}
  .contacts li{display:flex;align-items:center;gap:7px;height:19px}
  .contacts svg{flex:none}
</style>
</head>
<body>
<div class="canvas">

  <section class="card card--logo" aria-label="Logo side">
    <div class="brand">Brightwire Hollow</div>
    <div class="edge-rule">
      <span class="edge-rule__dark"></span>
      <span class="edge-rule__red"></span>
    </div>
  </section>

  <section class="card card--details" aria-label="Details side">
    <svg class="frame" width="540" height="308" viewBox="0 0 540 308">
      <polyline points="90,70 42,70 42,182 80,182 80,232" fill="none" stroke="#e8352a" stroke-width="2.5"/>
      <circle cx="80" cy="236" r="5" fill="#e8352a"/>
      <circle cx="94" cy="70" r="17" fill="#e8352a"/>
    </svg>

    <div class="name">Marcus <span class="name__last">Pell</span></div>

    <div class="social" aria-label="Social profiles">
      <span class="social__dot"></span>
      <span class="social__dot"></span>
      <span class="social__dot"></span>
    </div>

    <ul class="contacts">
      <li>
        <svg width="13" height="13" viewBox="0 0 13 13"><rect width="13" height="13" rx="2" fill="#e8352a"/><path d="M4 3.2l1.5 1.7-.8 1a5 5 0 0 0 2.4 2.4l1-.8 1.7 1.5-.9 1A6.5 6.5 0 0 1 3 4.1z" fill="#fff"/></svg>
        0431 587 219
      </li>
      <li>
        <svg width="13" height="13" viewBox="0 0 13 13"><rect width="13" height="13" rx="2" fill="#e8352a"/><rect x="2.5" y="4" width="8" height="5.5" fill="none" stroke="#fff" stroke-width="1"/><path d="M2.5 4l4 3 4-3" fill="none" stroke="#fff" stroke-width="1"/></svg>
        marcus@brightwirehollow.com.au
      </li>
      <li>
        <svg width="13" height="13" viewBox="0 0 13 13"><rect width="13" height="13" rx="2" fill="#e8352a"/><circle cx="6.5" cy="6.5" r="3.8" fill="none" stroke="#fff" stroke-width="1"/><path d="M2.7 6.5h7.6M6.5 2.7c-2 2.4-2 5.2 0 7.6M6.5 2.7c2 2.4 2 5.2 0 7.6" fill="none" stroke="#fff" stroke-width=".8"/></svg>
        brightwirehollow.com.au
      </li>
    </ul>

    <div class="tagline">24/7 Sydney Electrician</div>
  </section>

</div>
</body>
</html>
```